I'm looking for a logo design however launched a business card design project and just bundled the logo design project.

Kindly submit a proposal for a logo and business card so I can pay you for both designs. Here are what I need.

Please see attachment for our current logo design.

We need double side design card for our website promotion.

Logo Text

Tripquill482

```html
<!DOCTYPE html>
<html lang="en">
<head>
<meta charset="utf-8">
<title>Tripquill482 Business Card</title>
<link rel="stylesheet" href="https://fonts.googleapis.com/css2?family=Poppins:wght@600&family=Roboto:wght@400;500&display=swap">
<style>
  :root {
    --bg: #e9e9ec;
    --card-front: #2b1a6b;
    --card-back: #ffffff;
    --navy: #2b1a6b;
    --sky: #0a8bdc;
    --globe: #1a5fb8;
    --text-grey: #4a4a52;
    --white: #ffffff;
  }
  * { margin: 0; padding: 0; box-sizing: border-box; }
  html, body {
    width: 1200px; height: 912px; overflow: hidden;
    background: var(--bg);
    font-family: "Roboto", sans-serif;
  }
  .canvas { position: relative; width: 1200px; height: 912px; }
  .card {
    position: absolute;
    width: 600px; height: 343px;
    border-radius: 18px;
    box-shadow: 0 10px 28px rgba(0,0,0,0.18);
    overflow: hidden;
  }
  .card-front { left: 300px; top: 70px; background: var(--card-front); }
  .card-back { left: 300px; top: 497px; background: var(--card-back); }

  .brand {
    position: absolute;
    display: flex; align-items: center; gap: 16px;
    font-family: "Poppins", sans-serif; font-weight: 600;
  }
  .card-front .brand {
    left: 0; right: 0; top: 118px; justify-content: center;
    color: var(--white); font-size: 56px; letter-spacing: -1px;
  }
  .brand-dot { border-radius: 50%; background: var(--sky); flex: none; }
  .card-front .brand-dot { width: 52px; height: 52px; }
  .front-url {
    position: absolute; left: 0; right: 0; top: 250px;
    text-align: center; color: var(--white); font-size: 17px; letter-spacing: 0.5px;
  }

  .card-back .brand {
    left: 34px; top: 140px; flex-direction: column; gap: 14px;
    color: var(--navy); font-size: 30px;
  }
  .card-back .brand-dot { width: 96px; height: 96px; background: var(--globe); }
  .divider {
    position: absolute; left: 300px; top: 70px; width: 2px; height: 200px;
    background: var(--sky);
  }
  .contact { position: absolute; left: 330px; top: 62px; color: var(--text-grey); }
  .person-name { font-size: 25px; font-weight: 500; text-transform: uppercase; color: var(--navy); }
  .person-name .surname { color: var(--sky); }
  .person-role { font-size: 17px; margin-top: 2px; }
  .address { font-size: 16px; line-height: 1.45; margin-top: 16px; }
  .contact-list { list-style: none; margin-top: 14px; font-size: 16px; line-height: 1.6; }
  .contact-list li { display: flex; align-items: center; gap: 8px; }
  .contact-list svg { width: 13px; height: 13px; flex: none; }
  .web-accent { color: var(--sky); }
</style>
</head>
<body>
<main class="canvas">
  <section class="card card-front">
    <div class="brand"><span class="brand-dot"></span><span class="brand-name">Tripquill482</span></div>
    <p class="front-url">www.tripquill482.com</p>
  </section>

  <section class="card card-back">
    <div class="brand"><span class="brand-dot"></span><span class="brand-name">Tripquill482</span></div>
    <div class="divider"></div>
    <div class="contact">
      <h1 class="person-name">Daniel <span class="surname">Brooks</span></h1>
      <p class="person-role">Director</p>
      <p class="address">1820 Alder Lane NE<br>Maple Grove, MN 55311</p>
      <ul class="contact-list">
        <li><svg viewBox="0 0 16 16"><path d="M4 1l3 3-2 2c1 2 3 4 5 5l2-2 3 3-2 3C7 15 1 9 1 3z" fill="var(--navy)"/></svg>555-014-2290</li>
        <li><svg viewBox="0 0 16 16"><rect x="1" y="3" width="14" height="10" rx="1" fill="none" stroke="var(--navy)" stroke-width="1.6"/><path d="M1 4l7 5 7-5" fill="none" stroke="var(--navy)" stroke-width="1.6"/></svg>info@tripquill482.com</li>
        <li><svg viewBox="0 0 16 16"><circle cx="8" cy="8" r="6.5" fill="none" stroke="var(--navy)" stroke-width="1.5"/><path d="M1.5 8h13M8 1.5c-3 3-3 10 0 13M8 1.5c3 3 3 10 0 13" fill="none" stroke="var(--navy)" stroke-width="1.2"/></svg>www.<span class="web-accent">tripquill482</span>.com</li>
      </ul>
    </div>
  </section>
</main>
</body>
</html>
```